Interior design service, along with home organization, packing, and staging, home and business. As well as staging in conjunction with real estate sales.

Love many of your designs and will be choosing today. To inform you of the exact details needed, the name of the company is "Flourish by Marnie T" , my phone number and e-,ail need to be included. i also need either description or some sort of bullet points that give an idea of the following:

- Interior design for home and business
- Home organization and packing
- Staging for personal and professional space
- Real estate stagingĀ 

Thank you

Target Market(s)

wide audience, but most importantly people looking for a quality service

Industry/Entity Type

Real Estate

Contact Information for Business Card

Flourish By Marnie T
Marnie Toller
(555)617-3942
mtbriar@inboxly.example

Requirements
Must have
• I'm 29 so i want my card to reflect something professional but still fresh. I don't have any specific photos or quotes that Ive included, however I like the card to reflect a personal touch, which is what I'm seeking from this service in the design of my card. Thanks!

```html
<!DOCTYPE html>
<html lang="en">
<head>
<meta charset="utf-8">
<title>Flourish by Marnie T – Business Card</title>
<link rel="stylesheet" href="https://fonts.googleapis.com/css2?family=Petit+Formal+Script&display=swap">
<style>
  :root {
    --backdrop: #eceeed;
    --card: #050607;
    --name-grey: #9a9a9a;
    --text-white: #f2f2f2;
    --shadow: rgba(0, 0, 0, 0.18);
  }
  * { margin: 0; padding: 0; box-sizing: border-box; }
  html, body {
    width: 1200px;
    height: 702px;
    overflow: hidden;
    background: var(--backdrop);
  }
  .canvas {
    position: relative;
    width: 1200px;
    height: 702px;
    display: flex;
    align-items: center;
    justify-content: center;
    gap: 60px;
  }
  .card {
    position: relative;
    width: 490px;
    height: 280px;
    background: var(--card);
    box-shadow: 0 12px 30px var(--shadow);
    font-family: "Petit Formal Script", cursive;
    overflow: hidden;
  }
  .card-front .owner-name {
    position: absolute;
    left: 160px;
    top: 112px;
    font-size: 30px;
    color: var(--name-grey);
    white-space: nowrap;
  }
  .card-front .company-name {
    position: absolute;
    left: 200px;
    top: 162px;
    font-size: 15px;
    color: var(--name-grey);
    white-space: nowrap;
  }
  .card-back .services {
    position: absolute;
    left: 22px;
    top: 34px;
    color: var(--text-white);
    font-size: 12.5px;
    line-height: 1.6;
    white-space: nowrap;
  }
  .card-back .services .line-two { padding-left: 22px; }
  .card-back .contact {
    position: absolute;
    left: 130px;
    top: 120px;
    color: var(--text-white);
    font-size: 16px;
    line-height: 2;
    white-space: nowrap;
  }
</style>
</head>
<body>
  <main class="canvas">
    <section class="card card-front" aria-label="Card front">
      <p class="owner-name">Marnie Toller</p>
      <p class="company-name">Flourish by Marnie T</p>
    </section>
    <section class="card card-back" aria-label="Card back">
      <div class="services">
        <p class="line-one">Interior Design Service • Home Organization • Staging • Packing</p>
        <p class="line-two">Real Estate Sales &nbsp;• Home and Business</p>
      </div>
      <div class="contact">
        <p class="phone">Phone: (555)617-3942</p>
        <p class="email">Email: mtbriar@inboxly.example</p>
      </div>
    </section>
  </main>
</body>
</html>
```